Aerial Photography Business Card Design

I am looking for a business card for my drone photography business.

Contents should include
Back:
preferably a design involving one or more image(s) I have attached

OR logo and background of designer's choice

Front:
Tom Halvick
Aerial Photography
Real Estate, Construction, Inspection
FAA Certified Drone Pilot
Please include a simple logo for drone business.

Phone: 5185550147

Format should be .psd or .ai
please also include a copy as .pdf format.

```html
<!DOCTYPE html>
<html lang="en">
<head>
<meta charset="utf-8">
<title>Halcrest Photography – Business Card</title>
<link href="https://fonts.googleapis.com/css2?family=Poppins:wght@300;400;500;600;700&display=swap" rel="stylesheet">
<style>
  :root {
    --page-bg: #c9c9c9;
    --card-dark: #1d1d1d;
    --accent: #f47a20;
    --text-light: #f2f2f2;
    --text-muted: #d6d6d6;
    --shadow: rgba(0, 0, 0, 0.28);
    --tone-warm: #6b5a50;
    --tone-sand: #a89c8c;
    --tone-blue: #3a6fa8;
    --tone-green: #5d6a4c;
  }
  * { box-sizing: border-box; margin: 0; padding: 0; }
  html, body {
    width: 1200px; height: 900px; overflow: hidden;
    background: var(--page-bg);
    font-family: "Poppins", sans-serif;
  }
  .canvas { position: relative; width: 1200px; height: 900px; }

  .card {
    position: absolute; width: 560px; height: 320px;
    overflow: hidden; box-shadow: 0 12px 28px var(--shadow);
  }

  /* Back side: photo collage */
  .card-back { left: 80px; top: 90px; background: #333; }
  .collage {
    position: absolute; inset: 0;
    display: grid;
    grid-template-columns: 300px 260px;
    grid-template-rows: 110px 45px 165px;
  }
  .photo { width: 100%; height: 100%; }
  .photo-sunset {
    grid-column: 1; grid-row: 1 / 3;
    background: linear-gradient(180deg, #66605c 0%, var(--tone-warm) 100%);
  }
  .photo-pool {
    grid-column: 2; grid-row: 1;
    background: var(--tone-sand);
  }
  .photo-lake {
    grid-column: 2; grid-row: 2 / 4;
    background: linear-gradient(180deg, #5b86b6 0%, var(--tone-blue) 100%);
  }
  .photo-campus {
    grid-column: 1; grid-row: 3;
    background: var(--tone-green);
  }
  .back-logo {
    position: absolute; left: 218px; top: 128px;
    width: 158px; height: 54px;
    background: rgba(20, 20, 20, 0.85);
    border: 1px solid var(--accent);
    display: flex; align-items: center; justify-content: center; gap: 8px;
  }

  .brand-mark {
    border-radius: 50%; background: var(--accent); flex: none;
  }
  .brand-name {
    color: var(--accent); font-weight: 600; text-transform: uppercase;
    line-height: 1.05; letter-spacing: 0.06em; white-space: nowrap;
  }
  .back-logo .brand-mark { width: 18px; height: 18px; }
  .back-logo .brand-name { font-size: 11px; }

  /* Front side */
  .card-front { left: 560px; top: 470px; background: var(--card-dark); }
  .front-logo {
    position: absolute; left: 0; right: 0; top: 56px;
    display: flex; align-items: center; justify-content: center; gap: 16px;
  }
  .front-logo .brand-mark { width: 44px; height: 44px; }
  .front-logo .brand-name { font-size: 27px; }

  .details {
    position: absolute; left: 0; right: 0; top: 150px;
    display: flex; justify-content: center;
  }
  .person {
    text-align: right; padding-right: 14px;
    border-right: 1px solid #8a8a8a;
    padding-top: 22px;
  }
  .person-name {
    color: var(--accent); font-weight: 600; font-size: 15px;
    text-transform: uppercase; letter-spacing: 0.02em;
  }
  .person-role, .person-services {
    color: var(--text-muted); font-size: 11.5px; font-weight: 400; line-height: 1.45;
  }
  .contacts { list-style: none; padding-left: 12px; }
  .contacts li {
    display: flex; align-items: center; gap: 9px;
    color: var(--text-light); font-size: 11.5px; line-height: 1; height: 21px;
  }
  .contacts svg { width: 12px; height: 12px; flex: none; }

  .cert-band {
    position: absolute; left: 0; top: 250px; width: 340px; height: 24px;
    background: var(--accent); color: var(--text-light);
    font-size: 12px; font-weight: 500;
    display: flex; align-items: center; justify-content: flex-end; padding-right: 40px;
  }
  .accent-line {
    position: absolute; left: 340px; right: 0; top: 250px; height: 5px;
    background: var(--accent);
  }
</style>
</head>
<body>
<main class="canvas">

  <section class="card card-back">
    <div class="collage">
      <div class="photo photo-sunset" role="img" aria-label="Photo: drone flying against a sunset sky"></div>
      <div class="photo photo-pool" role="img" aria-label="Photo: top-down aerial view of a swimming pool"></div>
      <div class="photo photo-lake" role="img" aria-label="Photo: aerial view of a lake surrounded by forest"></div>
      <div class="photo photo-campus" role="img" aria-label="Photo: aerial view of a large building among trees"></div>
    </div>
    <div class="back-logo">
      <span class="brand-mark"></span>
      <span class="brand-name">Halcrest<br>Photography</span>
    </div>
  </section>

  <section class="card card-front">
    <div class="front-logo">
      <span class="brand-mark"></span>
      <span class="brand-name">Halcrest<br>Photography</span>
    </div>

    <div class="details">
      <div class="person">
        <p class="person-name">Tom Halvick</p>
        <p class="person-role">Aerial Photography</p>
        <p class="person-services">Real Estate, Construction, Inspection</p>
      </div>
      <ul class="contacts">
        <li>
          <svg viewBox="0 0 24 24" aria-hidden="true"><path fill="#f47a20" d="M6.6 10.8a15.1 15.1 0 0 0 6.6 6.6l2.2-2.2c.3-.3.7-.4 1-.2 1.1.4 2.3.6 3.6.6.6 0 1 .4 1 1V20c0 .6-.4 1-1 1A17 17 0 0 1 3 4c0-.6.4-1 1-1h3.5c.6 0 1 .4 1 1 0 1.3.2 2.5.6 3.6.1.3 0 .7-.2 1z"/></svg>
          5185550147
        </li>
        <li>
          <svg viewBox="0 0 24 24" aria-hidden="true"><rect x="2" y="5" width="20" height="14" fill="#f47a20"/><path d="M2 5l10 8 10-8" fill="none" stroke="#1d1d1d" stroke-width="2"/></svg>
          tom@halcrestphotography.com
        </li>
        <li>
          <svg viewBox="0 0 24 24" aria-hidden="true"><circle cx="12" cy="12" r="10" fill="#f47a20"/><path d="M2 12h20M12 2c3 3 3 17 0 20M12 2c-3 3-3 17 0 20" fill="none" stroke="#1d1d1d" stroke-width="1.4"/></svg>
          www.halcrestphotography.com
        </li>
      </ul>
    </div>

    <div class="cert-band">FAA Certified Drone Pilot</div>
    <div class="accent-line"></div>
  </section>

</main>
</body>
</html>
```